Lady Winnow's Cask Aged Heronfield Rum LABEL

Tallowbrook Distillery is looking for a label for our new product (Lady Winnow's Cask). This will be a barrel aged Rum that is distilled, bottled, and aged in small batches in Belmont, NC just outside of Charlotte, North Carolina. In the attached file (drink recipes) you will see the Product that we currently sell (Heronfield Rum). The new product does not have to be the same style, but we would like to maintain some brand relevance. There are some other attachments to give you an idea about the look of the company. Also attached is a picture of the dark rum in the bottle. This is what the label will go onto.

-The label will most likely be printed on craft paper stock.

Industry/Entity Type

It Company

Requirements
Must have
• We need the following in the new label
-Company Name= Tallowbrook Distillery
-Product name= Lady Winnow's Cask
-Product sub-name= Aged Heronfield Rum
-Product description= Distilled Bottled and Aged by Tallowbrook Distillery
Nice to have
• We would like to incorporate a rendering of Lady Winnow or just a crown. We think this is important because Charlotte, NC is named after her.

```html
<!DOCTYPE html>
<html lang="en">
<head>
<meta charset="utf-8">
<title>Lady Winnow's Cask — Aged Heronfield Rum Label</title>
<link rel="stylesheet" href="https://fonts.googleapis.com/css2?family=Cinzel:wght@400;600;700&display=swap">
<style>
  :root {
    --backdrop: #ffffff;
    --paper-light: #ecdfc2;
    --paper-mid: #e2d1ab;
    --paper-edge: #d3bd92;
    --ink-brown: #4b3420;
    --ink-dark: #1e1812;
  }
  * { margin: 0; padding: 0; box-sizing: border-box; }
  html, body {
    width: 1200px;
    height: 840px;
    overflow: hidden;
    background: var(--backdrop);
  }
  .canvas {
    position: relative;
    width: 1200px;
    height: 840px;
  }
  .label {
    position: absolute;
    left: 351px;
    top: 47px;
    width: 498px;
    height: 746px;
    background: radial-gradient(ellipse at 50% 45%, var(--paper-light) 0%, var(--paper-mid) 65%, var(--paper-edge) 100%);
    font-family: "Cinzel", serif;
    color: var(--ink-brown);
    text-align: center;
  }
  .brand-mark {
    position: absolute;
    left: 156px;
    top: 39px;
    width: 186px;
    height: 186px;
    border: 3px solid var(--ink-dark);
    border-radius: 50%;
    display: flex;
    align-items: center;
    justify-content: center;
  }
  .brand-mark__name {
    font-weight: 700;
    font-size: 22px;
    letter-spacing: 1px;
    color: var(--ink-dark);
  }
  .line {
    position: absolute;
    left: 0;
    width: 100%;
    white-space: nowrap;
    line-height: 1;
  }
  .distillery-name {
    top: 249px;
    font-size: 19px;
    font-weight: 600;
    letter-spacing: 0.5px;
    color: var(--ink-dark);
  }
  .rule {
    position: absolute;
    left: 54px;
    width: 390px;
    height: 0;
    border-top: 4px solid var(--ink-brown);
  }
  .rule--top { top: 308px; }
  .rule--bottom { top: 586px; }
  .product-name {
    font-size: 44px;
    font-weight: 600;
  }
  .product-name--1 { top: 336px; }
  .product-name--2 { top: 398px; }
  .product-name--3 { top: 460px; }
  .product-subname {
    top: 543px;
    font-size: 29px;
    font-weight: 600;
  }
  .description {
    top: 659px;
    font-size: 14px;
    color: var(--ink-dark);
  }
  .maker {
    top: 679px;
    font-size: 18px;
    font-weight: 600;
    color: var(--ink-dark);
  }
</style>
</head>
<body>
<main class="canvas">
  <section class="label">
    <div class="brand-mark">
      <span class="brand-mark__name">Tallowbrook</span>
    </div>

    <p class="line distillery-name">Tallowbrook Distillery</p>

    <div class="rule rule--top"></div>

    <h1>
      <span class="line product-name product-name--1">Lady</span>
      <span class="line product-name product-name--2">Winnow's</span>
      <span class="line product-name product-name--3">Cask</span>
    </h1>

    <h2 class="line product-subname">Aged Heronfield Rum</h2>

    <div class="rule rule--bottom"></div>

    <p class="line description">Distilled Bottled and Aged by</p>
    <p class="line maker">Tallowbrook Distillery</p>
  </section>
</main>
</body>
</html>
```